Flyer-Design für Physiotherapie-Praxis
Zielgruppe
Wir sind eine Praxis für Physiotherapie und möchten durch diesen Flyer neue Patienten werben. Der Flyer soll in Arztpraxen ausliegen und dort den Patienten direkt ansprechen und auf uns aufmerksam machen. Es ist auch eine Verknüpfung der Therapie mit einem Training in einem Gesundheitsstudio möglich, da im gleichen Haus das Physio Kraftwerk Eichenstetten beheimatet ist.
Aufgabenstellung
Der Fokus auf unsere Prinzipien (Ganzheitliche Therapie, hohes Maß an Therapiemöglichkeiten, Variation in den therapeutischen Ansätzen durch unterschiedlich fortgebildete Therapeuten, die nach den gleichen Idealen arbeiten)

```html
<!DOCTYPE html>
<html lang="de">
<head>
<meta charset="utf-8">
<title>Flyer – Zentrum für Therapie &amp; Training</title>
<link href="https://fonts.googleapis.com/css2?family=Source+Sans+3:wght@300;400;600;700;800&display=swap" rel="stylesheet">
<style>
  :root{
    --green:#c3d64b;
    --blue:#1f93d2;
    --navy:#2a2f6b;
    --ink:#1c1c1c;
    --white:#ffffff;
    --paper:#ffffff;
  }
  *{margin:0;padding:0;box-sizing:border-box}
  html,body{width:1200px;height:1200px;overflow:hidden;background:var(--paper)}
  body{position:relative;font-family:"Source Sans 3",sans-serif;color:var(--ink)}

  .panel{position:absolute;top:67px;width:511px;height:1072px;overflow:hidden;
    box-shadow:2px 4px 10px rgba(0,0,0,.25)}
  .panel--front{left:69px;background:var(--white)}
  .panel--inside{left:627px;background:var(--white)}

  .wave{position:absolute;left:0;top:0;width:511px;height:1072px}

  /* front */
  .brand{position:absolute;left:0;top:0;width:511px;height:260px;text-align:center}
  .brand__mark{position:absolute;left:225px;top:40px;width:62px;height:62px;border:3px solid var(--blue);border-radius:50%}
  .brand__line1{position:absolute;top:176px;width:100%;font-size:20px;line-height:1;font-weight:400;letter-spacing:.6px;color:var(--blue);white-space:nowrap}
  .brand__name{position:absolute;top:196px;width:100%;font-size:29px;line-height:1;font-weight:700;color:var(--navy);white-space:nowrap}
  .brand__owner{position:absolute;top:228px;width:100%;font-size:18px;line-height:1;font-weight:400;color:var(--blue)}

  .photo{position:absolute}
  .photo--team{left:0;top:260px;width:511px;height:420px;
    background:linear-gradient(180deg,#c9d2dc 0%,#a9cfe8 45%,#8fbfe0 75%,#6f7f8f 100%)}
  .photo--pool{left:46px;top:229px;width:419px;height:279px;
    background:linear-gradient(180deg,#eef1f2 0%,#d9e6dd 40%,#5dbbd9 65%,#2f93c4 85%,#9aa3a6 100%)}
  .photo--gym{left:46px;top:849px;width:419px;height:185px;
    background:linear-gradient(180deg,#e9e6df 0%,#c9c9c6 45%,#9c9d9f 75%,#6d6e70 100%)}

  .badge{position:absolute;width:128px;height:128px;border-radius:50%;background:var(--blue);
    color:var(--white);display:flex;flex-direction:column;justify-content:center;align-items:center;text-align:center;line-height:1.2}
  .badge--front{left:313px;top:543px;transform:rotate(-8deg);font-size:14px;font-weight:400}
  .badge--front b{font-weight:700}
  .badge--inside{left:248px;top:443px;transform:rotate(9deg);font-size:13px;font-weight:400;text-transform:uppercase}
  .badge--inside b{font-weight:800}

  .headline{position:absolute;left:66px;width:381px;color:var(--white);line-height:1;white-space:nowrap}
  .headline--front{top:706px}
  .headline__light{display:block;font-size:37px;font-weight:300;letter-spacing:-.6px}
  .headline__bold{display:block;font-size:38px;font-weight:800;letter-spacing:-.3px;margin-top:2px}

  .copy{position:absolute;left:66px;width:381px;font-size:14px;line-height:17.3px;font-weight:300;
    text-align:justify;hyphens:auto}
  .copy--front{top:792px;color:var(--white)}
  .copy--front strong{font-weight:700}

  .rule{position:absolute;left:66px;width:381px;height:1.5px;background:var(--white);top:977px}
  .contact{position:absolute;left:66px;width:381px;top:990px;color:var(--white);font-size:12px;line-height:18px;font-weight:300;font-style:normal;white-space:nowrap}
  .contact strong{font-weight:700}

  /* inside */
  .section-title{position:absolute;line-height:1.05;white-space:nowrap}
  .section-title--therapy{left:46px;top:44px;color:var(--white)}
  .section-title--training{right:46px;top:578px;color:var(--green);text-align:right}
  .section-title__light{display:block;font-size:25px;font-weight:300}
  .section-title__bold{display:block;font-size:29px;font-weight:800}

  .copy--therapy{left:46px;width:419px;top:111px;color:var(--white)}
  .copy--therapy strong{font-weight:700}
  .copy--training{left:46px;width:419px;top:644px;color:var(--ink);font-weight:400}
  .copy--training strong{font-weight:700}

  .footer-line{position:absolute;left:0;top:1053px;width:511px;height:1.5px;background:var(--green)}
</style>
</head>
<body>

<section class="panel panel--front">
  <div class="photo photo--team" role="img" aria-label="Teamfoto: Therapeutinnen und Therapeuten in hellblauen Poloshirts vor Kletterwand"></div>
  <svg class="wave" viewBox="0 0 511 1072" aria-hidden="true">
    <path d="M0,620 C120,680 230,720 340,660 C420,618 470,630 511,658 L511,1072 L0,1072 Z" fill="var(--green)"/>
    <path d="M0,612 C110,650 220,680 320,640 C410,602 465,610 511,640" fill="none" stroke="var(--white)" stroke-width="1.5"/>
  </svg>

  <header class="brand">
    <div class="brand__mark"></div>
    <div class="brand__line1">ZENTRUM FÜR THERAPIE &amp; TRAINING</div>
    <div class="brand__name">Lorenz Vogt &amp; Helga Sanner</div>
    <div class="brand__owner">Inhaber: Helga Sanner</div>
  </header>

  <div class="badge badge--front"><b>Seit über</b><b>50 Jahren -</b>ein Zeichen für<br>Qualität und<br>Vertrauen</div>

  <h1 class="headline headline--front">
    <span class="headline__light">WIR SIND THERAPEUTEN</span>
    <span class="headline__bold">AUS ÜBERZEUGUNG!</span>
  </h1>

  <p class="copy copy--front"><strong>Unsere Praxis gibt es seit 1969. In dieser Zeit konnten wir viel Erfahrung sammeln.</strong> Wir sind ein Team aus älteren und jüngeren Therapeuten, aus Masseuren, med. Bademeistern und Physiotherapeuten. Diese bunte Mischung beinhaltet viel Erfahrung und viel Wissen. Beides wird in regelmäßigen internen Fortbildungen ausgetauscht. So ergänzen wir uns gegenseitig. Wir arbeiten als Team Hand in Hand und schätzen das Fachwissen jedes einzelnen Kollegen. Wir sind motiviert und mit Freude bei der Arbeit, denn wir wissen, was unsere Patienten mit Hilfe der Physiotherapie erreichen können.</p>

  <div class="rule"></div>
  <address class="contact">
    <strong>Zentrum für Therapie und Training Lorenz Vogt &amp; Helga Sanner</strong><br>
    <strong>Inhaber: Helga Sanner</strong> • Obere Gasse 27 • 90312 Lindenau-Eichenstetten<br>
    Telefon: 0912-480276 • Telefax: 0912-4802799 • anmeldung@praxis-vogt.de
  </address>
</section>

<section class="panel panel--inside">
  <svg class="wave" viewBox="0 0 511 1072" aria-hidden="true">
    <path d="M0,0 H511 V500 C450,488 380,480 300,520 C200,575 90,592 0,578 Z" fill="var(--green)"/>
    <path d="M0,527 C100,565 200,562 300,512 C380,472 450,464 511,472" fill="none" stroke="var(--white)" stroke-width="1.5"/>
  </svg>

  <h2 class="section-title section-title--therapy">
    <span class="section-title__light">VIELEZAHL VON</span>
    <span class="section-title__bold">THERAPIEMÖGLICHKEITEN</span>
  </h2>
  <p class="copy copy--therapy">Wir haben eine <strong>Vielzahl von Therapiegeräten</strong> und -hilfsmitteln zur Verfügung, z.B. eine Kletterwand, Sling Trainer, eine Vibrala®-Rüttelplatte, ein Balance-Gestell und ein <strong>Bewegungsbad!</strong> Im 32°C warmem Wasser können sich unsere Patienten besser bewegen. Mit unserem Fachwissen und unserer Erfahrung haben wir uns auf die Behandlung orthopädischer, chirurgischer und neurologischer Patienten spezialisiert.</p>

  <div class="photo photo--pool" role="img" aria-label="Bewegungsbad mit Geländer in hellem Raum mit Pflanzen und Glasfront"></div>

  <div class="badge badge--inside">Wir haben<br><span><b>das Ziel</b>, zu den</span>besten unseres<br>Fachs zu<br>gehören</div>

  <h2 class="section-title section-title--training">
    <span class="section-title__light">AKTIVES</span>
    <span class="section-title__bold">GESUNDHEITSTRAINING</span>
  </h2>
  <p class="copy copy--training">Für gute Fortschritte in der Therapie und die Erhaltung dieser Fortschritte ist der Weg zur sportlichen Aktivität essentiell. Diesen Weg erleichtern wir unseren Patienten durch unser Angebot des <strong>Aktiven Gesundheitstrainings</strong>. Zusätzlich zu Ihrem Rezept erhalten unsere neuen Patienten einen zusätzlichen und kostenfreien Beratungstermin im Physio Kraftwerk Eichenstetten. In diesem Termin zeigen wir Ihnen Möglichkeiten, selbst etwas zu Ihrer Gesundung beizutragen. Je nachdem, was Ihnen gerade am effektivsten hilft, trainieren Sie 6 x am Kraft-Ausdauer-Zirkel der Firma Torvanta oder am Flexavo-Zirkel. Das Training an diesen Geräten ist einfach, sicher und effektiv. Da das Training maximal 35 Minuten Zeit beansprucht ist Zeitmangel kein Argument mehr.</p>

  <div class="photo photo--gym" role="img" aria-label="Trainingsraum mit Kraft- und Ausdauergeräten im Zirkel"></div>

  <div class="footer-line"></div>
</section>

</body>
</html>
```